Corbrook Estates LLC stationary for a real estate property management company.

Create stationary (letterhead, envelopes, business cards) using Corbrook Estates LLC logo as primary creative element. Stationary design needs to be horizontal, leaving as much space as possible for correspondence copy. See attached Creative Brief and past stationary files for details.

Target Market(s)

Prospective apartment residents and current residents, vendors, and government agencies.

Industry/Entity Type

Property Management

Contact Information for Business Card

Business card employee title: Property Manager. Should include address, phone, fax, email, website, slogan, and Corbrook Estates logo.

Font styles to use
Sans Serif

Colors
0592cd
000000

Requirements
Must have
• Tone should be conservative, institutional, business (i.e. banking, finance, real estate). Must include: address, phone, fax, website, and slogan (see attached Creative Brief). Should be a horizontal design, leaving as much room as possible for letter correspondence copy.
Nice to have
• Please use an Arial or Helvetica style font.
Should not have
• Letterhead layout should leave as much room as possible for copy.

```html
<!DOCTYPE html>
<html lang="en">
<head>
<meta charset="utf-8">
<title>Corbrook Estates LLC – Stationery</title>
<link href="https://fonts.googleapis.com/css2?family=Arimo:wght@400;700&family=Roboto+Condensed:wght@400&display=swap" rel="stylesheet">
<style>
  :root {
    --brand-blue: #1a8ec8;
    --brand-blue-dark: #0f6fae;
    --ink: #222222;
    --charcoal: #444a50;
    --paper: #ffffff;
    --backdrop: #ececec;
  }
  * { box-sizing: border-box; margin: 0; padding: 0; }
  html, body { width: 1200px; height: 900px; overflow: hidden; }
  body { background: var(--backdrop); font-family: "Arimo", Arial, sans-serif; color: var(--ink); position: relative; }

  .sheet { position: absolute; background: var(--paper); overflow: hidden; box-shadow: 0 2px 6px rgba(0,0,0,0.12); }

  .wordmark { display: flex; align-items: center; gap: 6px; font-family: "Arimo", Arial, sans-serif; font-weight: 700; text-transform: uppercase; color: var(--brand-blue-dark); white-space: nowrap; }
  .wordmark__dot { border-radius: 50%; background: currentColor; flex: none; }
  .wordmark--light { color: var(--paper); }

  /* Business card front */
  .card-front { left: 152px; top: 86px; width: 215px; height: 123px; }
  .card-front .wordmark { position: absolute; right: 12px; top: 22px; font-size: 7.5px; gap: 4px; }
  .card-front .wordmark__dot { width: 10px; height: 10px; }
  .card-front__name { position: absolute; left: 17px; top: 32px; font-size: 10px; font-weight: 700; color: #1d2a44; }
  .card-front__details { position: absolute; left: 17px; top: 50px; list-style: none; font-size: 7px; line-height: 9.5px; color: var(--ink); }
  .card-front__details li { display: flex; align-items: center; gap: 5px; }
  .card-front__details svg { width: 6px; height: 6px; flex: none; }
  .card-front__details .no-icon { padding-left: 11px; }
  .card-front__band { position: absolute; left: 0; bottom: 0; width: 100%; height: 13px; background: var(--brand-blue); }

  /* Business card back */
  .card-back { left: 378px; top: 86px; width: 215px; height: 123px; background: var(--brand-blue); }
  .card-back .wordmark { position: absolute; left: 0; right: 0; top: 50px; justify-content: center; font-size: 13px; }
  .card-back .wordmark__dot { width: 18px; height: 18px; }
  .card-back__web { position: absolute; left: 0; right: 0; top: 101px; text-align: center; font-size: 6.5px; letter-spacing: 1px; color: #d8ecf7; text-transform: uppercase; }

  /* Envelope front */
  .envelope-front { left: 59px; top: 246px; width: 533px; height: 266px; }
  .envelope-front .wordmark { position: absolute; left: 8px; top: 26px; font-size: 19px; }
  .envelope-front .wordmark__dot { width: 36px; height: 36px; }
  .envelope-front__address { position: absolute; left: 22px; top: 77px; font-family: "Roboto Condensed", Arial, sans-serif; font-size: 8.5px; letter-spacing: -0.1px; }
  .envelope-front__band { position: absolute; left: 0; bottom: 0; width: 450px; height: 22px; background: var(--brand-blue); }
  .corner-disc { position: absolute; border-radius: 50%; border: 5px solid var(--charcoal); background: var(--brand-blue-dark); }
  .envelope-front .corner-disc { width: 100px; height: 100px; left: 443px; top: 172px; }

  /* Envelope back */
  .envelope-back { left: 59px; top: 538px; width: 533px; height: 265px; }
  .envelope-back__flap { position: absolute; left: 0; top: 0; width: 533px; height: 108px; }
  .envelope-back .wordmark { position: absolute; left: 0; right: 0; top: 34px; justify-content: center; font-size: 19px; }
  .envelope-back .wordmark__dot { width: 36px; height: 36px; }

  /* Letterhead */
  .letterhead { left: 630px; top: 83px; width: 508px; height: 721px; }
  .letterhead__top { position: absolute; left: 0; top: 0; width: 508px; height: 22px; }
  .letterhead .wordmark { position: absolute; left: 12px; top: 32px; font-size: 19px; }
  .letterhead .wordmark__dot { width: 36px; height: 36px; }
  .letterhead__footer-info { position: absolute; right: 103px; top: 683px; font-family: "Roboto Condensed", Arial, sans-serif; font-size: 8.5px; letter-spacing: -0.1px; white-space: nowrap; }
  .letterhead__band { position: absolute; left: 0; bottom: 0; width: 420px; height: 19px; background: var(--brand-blue); }
  .letterhead__web { position: absolute; right: 100px; bottom: 4px; font-size: 8.5px; letter-spacing: 1.3px; color: var(--paper); }
  .letterhead .corner-disc { width: 100px; height: 100px; left: 416px; top: 630px; }
</style>
</head>
<body>

  <section class="sheet card-front" aria-label="Business card, front">
    <div class="wordmark"><span class="wordmark__dot"></span>Corbrook Estates LLC</div>
    <p class="card-front__name">Alan Reyes</p>
    <ul class="card-front__details">
      <li><svg viewBox="0 0 10 10"><path d="M5 0a3.5 3.5 0 0 0-3.5 3.5C1.5 6 5 10 5 10s3.5-4 3.5-6.5A3.5 3.5 0 0 0 5 0zm0 5a1.4 1.4 0 1 1 0-2.8A1.4 1.4 0 0 1 5 5z" fill="#222"/></svg>18320 Harlow Ave</li>
      <li><svg viewBox="0 0 10 10"><path d="M2 0l2 2.5-1 1.3c.6 1.3 1.6 2.3 2.9 2.9L7.2 5.8 10 7.8 8.8 10C4 9.5.4 5.9 0 1.2z" fill="#222"/></svg>5550142288</li>
      <li class="no-icon">5550139041</li>
      <li><svg viewBox="0 0 10 10"><rect x="0.5" y="1.5" width="9" height="7" fill="none" stroke="#222"/><path d="M0.5 1.5l4.5 4 4.5-4" fill="none" stroke="#222"/></svg>areyes@corbrookmail.com</li>
    </ul>
    <div class="card-front__band"></div>
  </section>

  <section class="sheet card-back" aria-label="Business card, back">
    <div class="wordmark wordmark--light"><span class="wordmark__dot"></span>Corbrook Estates LLC</div>
    <p class="card-back__web">www.corbrookestates.com</p>
  </section>

  <section class="sheet envelope-front" aria-label="Envelope, front">
    <div class="wordmark"><span class="wordmark__dot"></span>Corbrook Estates LLC</div>
    <p class="envelope-front__address">2750 Harbor Ridge Rd. #310,&nbsp; Lakemont, CA 90417</p>
    <div class="envelope-front__band"></div>
    <div class="corner-disc"></div>
  </section>

  <section class="sheet envelope-back" aria-label="Envelope, back">
    <svg class="envelope-back__flap" viewBox="0 0 533 108" preserveAspectRatio="none">
      <path d="M0 0H533L527 44Q523 88 508 100Q500 107 488 107H45Q33 107 25 100Q12 88 10 44Z" fill="var(--brand-blue)"/>
    </svg>
    <div class="wordmark wordmark--light"><span class="wordmark__dot"></span>Corbrook Estates LLC</div>
  </section>

  <section class="sheet letterhead" aria-label="Letterhead">
    <svg class="letterhead__top" viewBox="0 0 508 22" preserveAspectRatio="none">
      <polygon points="0,0 508,0 508,6 0,22" fill="var(--brand-blue-dark)"/>
      <polygon points="320,14 508,7 508,21" fill="var(--charcoal)"/>
    </svg>
    <div class="wordmark"><span class="wordmark__dot"></span>Corbrook Estates LLC</div>
    <p class="letterhead__footer-info">2750 Harbor Ridge Rd. #310 &nbsp;|&nbsp; Lakemont, CA 90417 &nbsp;|&nbsp; 555-014-7720 ph &nbsp;|&nbsp; 555-014-7721 fx</p>
    <div class="letterhead__band"></div>
    <p class="letterhead__web">www.corbrookestates.us</p>
    <div class="corner-disc"></div>
  </section>

</body>
</html>
```